Semi Permanent make up flyer

Hi

I will be sending a few thousand flyers dropped door to door in some very lovely parts of London.

The flyer must contain the following information;

New studio in Greenwich

Velline Arc trained technician - gold advanced level

Free consultation no obligation

Price List;
Eyebrow hair stroke: £325
Eyebrows 3D effect: £395
Microblading hair stroke: £330
Eyelash enhancement Top: £250
Eyelash enhancement Top & Bottom: £300
Lip blush: £450

Tel;……………….
Facebook: Odrelle Permanent Cosmetics
Instagram: Odrelle_Permanent_Cosmetics

Special introductory offers - available for a limited time only;
Like & share my page for 10% off any treatment
Refer a friend for £50 off each
Buy one treatment get 50% off another

I would like it to look clean, professional, expensive, and high end/luxury

I’m happy to make this a double sided print so I can have my logo on the front and the information on the back.

It must include my logo.

If you could use images of appealing women I think it would work best. Images have to have nice eyes, lips and brows. Weather you use entire face or features that is up to you.

Please show me a selection of different colour ways across the whole design. I personally feel softer tones would work. No black or bright colours.

I will be getting my new phone number in the next few days. I will let you know via messages what it is for you to add it in.

Any questions feel free to ask.

Target Market(s)

Women

Industry/Entity Type

Beauty Salon

Font styles to use
Sans Serif

Requirements
Must have
• Everything in Description
Nice to have
• The designers give their ideas. Im looking for input
Should not have
• Childish, cheap images or fonts. This is very high end so needs to look it

```html
<!DOCTYPE html>
<html lang="en">
<head>
<meta charset="utf-8">
<title>Odrelle Permanent Cosmetics – Flyer</title>
<link rel="stylesheet" href="https://fonts.googleapis.com/css2?family=Great+Vibes&family=Lato:ital,wght@1,700&family=Exo+2:wght@400;500;600;700&display=swap">
<style>
  :root {
    --page-bg: #ece9e4;
    --paper-light: #ffffff;
    --paper-grey: #e2e2e2;
    --orange: #f0a21e;
    --orange-deep: #e08a12;
    --charcoal: #2b2b2b;
    --ink: #1b1b1b;
    --ring-grey: #7a7a7a;
    --white: #ffffff;
  }
  * { margin: 0; padding: 0; box-sizing: border-box; }
  html, body { width: 825px; height: 1200px; overflow: hidden; background: var(--page-bg); }
  .canvas { position: relative; width: 825px; height: 1200px; }
  .flyer {
    position: absolute; left: 90px; top: 143px; width: 647px; height: 914px;
    overflow: hidden; font-family: "Exo 2", sans-serif; color: var(--ink);
    background: linear-gradient(180deg, var(--paper-light) 0%, var(--paper-grey) 45%, var(--paper-light) 100%);
  }
  .flyer-shapes { position: absolute; inset: 0; }
  .studio-banner {
    position: absolute; left: 0; top: 35px; width: 460px; height: 62px;
    background: linear-gradient(180deg, #f6b53a, var(--orange-deep));
    border: 2px solid var(--charcoal); border-left: none;
    border-radius: 0 31px 31px 0;
    display: flex; align-items: center; padding-left: 42px;
  }
  .studio-banner h2 {
    font-family: "Great Vibes", cursive; font-weight: 400; font-size: 40px;
    color: var(--white); line-height: 1;
  }
  .credential {
    position: absolute; left: 47px; top: 120px; width: 380px;
    font-family: "Lato", sans-serif; font-style: italic; font-weight: 700;
    font-size: 29px; line-height: 37px; color: var(--ink);
  }
  .photo { position: absolute; }
  .photo-model {
    left: 470px; top: 0; width: 177px; height: 212px;
    background: radial-gradient(circle at 50% 45%, #e9c2ad 0%, #d9a78f 40%, #f3f3f3 75%);
  }
  .photo-circle { border-radius: 50%; }
  .photo-eye {
    left: 32px; top: 244px; width: 192px; height: 192px;
    border: 12px solid var(--ring-grey);
    background: radial-gradient(circle, #6d7a64 0%, #bdb0b2 45%, #dcd3d6 100%);
  }
  .photo-lips {
    left: 214px; top: 228px; width: 126px; height: 126px;
    border: 10px solid var(--ring-grey);
    background: radial-gradient(circle, #e27a6d 0%, #d4655b 55%, #c49a8d 100%);
  }
  .photo-face-a {
    left: 346px; top: 770px; width: 120px; height: 120px;
    border: 6px solid var(--orange);
    background: radial-gradient(circle, #f4ddd0 0%, #e9c9b9 60%, #dcdcdc 100%);
  }
  .photo-face-b {
    left: 490px; top: 770px; width: 120px; height: 120px;
    border: 6px solid var(--orange);
    background: radial-gradient(circle, #d9a88c 0%, #6b3f2a 60%, #3a2418 100%);
  }
  .consultation { position: absolute; left: 333px; top: 324px; }
  .consultation p { font-size: 31px; font-weight: 500; color: var(--white); line-height: 38px; }
  .consultation strong { display: block; font-size: 42px; font-weight: 500; color: var(--orange); line-height: 48px; }
  .price-list {
    position: absolute; left: 315px; top: 440px; width: 288px;
    border: 2px solid var(--orange); border-radius: 16px; padding: 4px 0;
  }
  .price-list li {
    list-style: none; display: flex; justify-content: space-between; align-items: center;
    padding: 0 18px; min-height: 32px; font-size: 13.5px; color: var(--white);
    border-bottom: 1.5px solid var(--orange);
  }
  .price-list li:last-child { border-bottom: none; }
  .price-list li.tall { min-height: 42px; line-height: 15px; }
  .price-list .price { width: 44px; }
  .offer-refer { position: absolute; left: 35px; top: 476px; color: var(--ink); }
  .offer-refer p { font-size: 20px; font-weight: 700; line-height: 24px; }
  .offer-refer strong { display: block; font-size: 29px; font-weight: 700; line-height: 36px; }
  .offer-bogo {
    position: absolute; left: 35px; top: 564px; font-size: 18px; font-weight: 700; line-height: 24px;
  }
  .brand-name {
    position: absolute; left: 37px; top: 658px; width: 190px;
    font-size: 20px; font-weight: 600; line-height: 24px; color: var(--ink);
  }
  .offer-social { position: absolute; left: 290px; top: 682px; width: 324px; text-align: center; }
  .offer-social p { font-size: 26px; font-weight: 500; color: var(--white); line-height: 32px; }
  .offer-social strong { display: block; font-size: 22px; font-weight: 500; color: var(--orange); line-height: 30px; }
  .contact { position: absolute; left: 25px; top: 810px; font-size: 18px; font-weight: 500; color: var(--charcoal); }
  .contact li { list-style: none; display: flex; align-items: center; gap: 8px; height: 30px; }
  .contact .dot { width: 20px; height: 20px; border-radius: 50%; border: 1.5px solid var(--charcoal); }
  .contact .tel { margin-bottom: 2px; }
</style>
</head>
<body>
<div class="canvas">
  <section class="flyer">
    <svg class="flyer-shapes" width="647" height="914" viewBox="0 0 647 914" aria-hidden="true">
      <defs>
        <linearGradient id="orangeFill" x1="0" y1="0" x2="0" y2="1">
          <stop offset="0" stop-color="#f6b53a"/>
          <stop offset="1" stop-color="#e08a12"/>
        </linearGradient>
        <linearGradient id="darkFill" x1="0" y1="0" x2="1" y2="1">
          <stop offset="0" stop-color="#3d3d3d"/>
          <stop offset="1" stop-color="#232323"/>
        </linearGradient>
      </defs>
      <path d="M647,185 C540,250 380,215 245,255 C300,230 330,200 340,170 C360,220 470,215 647,175 Z" fill="url(#orangeFill)"/>
      <path d="M0,300 C70,262 170,250 245,262 C232,360 238,560 215,790 L0,790 Z" fill="url(#orangeFill)"/>
      <path d="M245,262 C232,360 238,560 215,790 L232,790 C255,560 250,360 262,268 Z" fill="#ffffff"/>
      <path d="M647,192 C540,255 380,235 262,268 C250,360 255,560 232,790 C380,770 520,790 647,760 Z" fill="url(#darkFill)"/>
      <rect x="0" y="558" width="250" height="58" fill="#ffffff"/>
      <path d="M0,782 C200,750 420,815 647,765 L647,914 L0,914 Z" fill="#f0f0f0"/>
      <path d="M0,782 C200,750 420,815 647,765" fill="none" stroke="#f0a21e" stroke-width="5"/>
    </svg>

    <div class="studio-banner"><h2>New studio in Greenwich</h2></div>
    <h1 class="credential">Velline Arc<br>trained technician - gold<br>advanced level</h1>

    <div class="photo photo-model" role="img" aria-label="Model with purple eye make-up and painted nails"></div>
    <div class="photo photo-circle photo-eye" role="img" aria-label="Close-up of an eye with eyeliner enhancement"></div>
    <div class="photo photo-circle photo-lips" role="img" aria-label="Close-up of lips after lip blush"></div>

    <div class="consultation">
      <p>Free consultation<strong>No obligation</strong></p>
    </div>

    <ul class="price-list">
      <li><span>Eyebrow hair stroke</span><span class="price">£325</span></li>
      <li><span>Eyebrows 3D effect</span><span class="price">£395</span></li>
      <li><span>Microblading hair stroke</span><span class="price">£330</span></li>
      <li><span>Eyelash enhancement Top</span><span class="price">£250</span></li>
      <li class="tall"><span>Eyelash enhancement<br>Top &amp; Bottom</span><span class="price">£300</span></li>
      <li><span>Lip blush</span><span class="price">£450</span></li>
    </ul>

    <div class="offer-refer"><p>Refer a friend for<strong>£50 off each</strong></p></div>
    <p class="offer-bogo">Buy one treatment<br>get 50% off another</p>

    <p class="brand-name">Odrelle Permanent Cosmetics</p>

    <div class="offer-social"><p>Like &amp; share my page<strong>for 10% off any treatment</strong></p></div>

    <ul class="contact">
      <li class="tel">Tel:..................</li>
      <li><span class="dot"></span>Odrelle Permanent Cosmetics</li>
      <li><span class="dot"></span>Odrelle_Permanent_Cosmetics</li>
    </ul>

    <div class="photo photo-circle photo-face-a" role="img" aria-label="Portrait of a woman with natural make-up"></div>
    <div class="photo photo-circle photo-face-b" role="img" aria-label="Portrait of a woman with red lips and styled hair"></div>
  </section>
</div>
</body>
</html>
```